KLT Flyer - Workshop and Scholarship Program

KLT needs a double sided flyer designed for an upcoming workshop we have that is also doubling as a launch of our business and of our scholarship program.
All of the information required to go onto the flyer is contained below in the two documents.
The first is a word document that contains the details to be included on the flyer - this is in the order that I wish to present them also.
The second document is an earlier example of a winning flyer that was designed for an earlier launch. I was happy with many of the characteristics within this flyer including the photo/bio at the bottom.
Please note that the language and descriptions have all changed.
Please use images and patterns that you feel address the requirements of the advertisement.
I have included the original design files for the logo and flyer to get the logo and bio image
Target Market(s)
HSC students (Final Year of High School
Industry/Entity Type
Education
Font styles to use
Other font styles liked:
- Myriad Pro
Requirements
Must have
- The logo of the business must be shown a maximum of twice on both sides. Please remove the surrounding square and imbed it into the flyer.
- A simple but effective design
Nice to have
- Images that reflect the content
Should not have
- Too much going on that the message is lost.

```html
<!DOCTYPE html>
<html lang="en">
<head>
<meta charset="utf-8">
<title>KLT Flyer – HSC Workshop and Scholarship Program</title>
<link href="https://fonts.googleapis.com/css2?family=Oswald:wght@400;500;600&family=PT+Sans+Narrow:wght@400;700&family=Source+Sans+3:wght@400;600;700&display=swap" rel="stylesheet">
<style>
:root{
  --orange:#f47a16;
  --orange-dark:#e4670a;
  --ink:#1d1d1d;
  --black:#151515;
  --grey-panel:#e9e9e9;
  --grey-cell:#dcdcdc;
  --navy:#1f3553;
  --stage:#ececec;
  --white:#ffffff;
}
*{box-sizing:border-box;margin:0;padding:0}
html,body{width:1200px;height:1200px;overflow:hidden}
body{background:var(--stage);position:relative;font-family:"PT Sans Narrow",sans-serif;color:var(--ink)}
.sheet{position:absolute;background:var(--white);overflow:hidden}
.sheet--front{left:112px;top:254px;width:452px;height:640px}
.sheet--back{left:658px;top:258px;width:438px;height:632px}
.side-label{position:absolute;top:956px;font-family:"Source Sans 3",sans-serif;font-weight:600;font-size:22px;letter-spacing:.5px;color:var(--black)}
.side-label--front{left:283px}
.side-label--back{left:900px}

/* brand */
.brand{position:absolute;display:flex;align-items:center;gap:6px;font-family:"Source Sans 3",sans-serif;font-weight:700;font-size:22px;color:var(--navy)}
.brand__dot{width:14px;height:14px;border-radius:50%;background:var(--orange)}

/* photo placeholders */
.photo{position:absolute}

/* front: headline band */
.headline{position:absolute;left:0;top:218px;width:452px;height:106px}
.headline__orange{position:absolute;left:0;top:0;width:250px;height:106px;background:var(--orange);clip-path:polygon(0 0,100% 0,96% 100%,0 100%)}
.headline__black{position:absolute;left:236px;top:12px;width:216px;height:94px;background:linear-gradient(90deg,#2a2a2a,#111);clip-path:polygon(4% 0,100% 0,100% 100%,0 100%)}
.headline__year{position:absolute;left:16px;top:8px;font-family:"Oswald",sans-serif;font-weight:600;font-size:33px;line-height:1;color:var(--white)}
.headline__title{position:absolute;left:16px;top:46px;font-family:"Oswald",sans-serif;font-weight:400;font-size:18px;line-height:25px;color:var(--ink);letter-spacing:-.2px}
.headline__tag{position:absolute;left:264px;font-family:"PT Sans Narrow",sans-serif}
.tag--orange{color:var(--orange);font-weight:700;font-size:10.5px}
.tag--white{color:var(--white);font-size:15px;font-family:"Source Sans 3",sans-serif}

/* front body */
.info-panel{position:absolute;left:0;top:324px;width:236px;height:226px;background:linear-gradient(180deg,#fafafa,#e3e3e3)}
.info-panel h3,.reg-title{font-family:"Source Sans 3",sans-serif;font-weight:700;color:var(--orange);font-size:8.5px}
.info-panel h3{position:absolute;left:10px;top:10px}
.bullets{position:absolute;font-size:5.6px;line-height:7.2px;color:#333;list-style:none}
.bullets li{padding-left:6px;position:relative}
.bullets li::before{content:"";position:absolute;left:0;top:2.5px;width:2.5px;height:2.5px;border-radius:50%;background:var(--orange)}
.info-panel p{position:absolute;font-size:6px;color:#333}
.info-panel .strong{font-weight:700;color:var(--ink)}

.sessions{position:absolute;font-family:"PT Sans Narrow",sans-serif}
.sessions h4{font-family:"Source Sans 3",sans-serif;font-weight:600;font-size:10px;text-align:center;margin-bottom:5px}
.row{display:flex;align-items:flex-start;margin-bottom:5px}
.row__label{flex:0 0 auto;font-family:"Source Sans 3",sans-serif;font-weight:600;font-size:6px;padding:2px 4px;height:12px}
.row__value{font-size:5.4px;line-height:6.4px;color:#333;padding:2px 6px}
.row--orange .row__label{background:var(--orange);color:var(--white)}
.row--grey{background:var(--grey-cell)}
.row--grey .row__label{background:transparent;color:#333}

.owner-photo{position:absolute;left:13px;top:494px;width:94px;height:126px;border:2px solid var(--orange);background:linear-gradient(160deg,#d9d2c8,#9a8c7e 55%,#6f86a4)}
.owner-name{position:absolute;left:115px;top:514px;font-family:"Source Sans 3",sans-serif;font-weight:700;font-size:6.6px;line-height:8px}
.footer-band{position:absolute;left:0;top:550px;width:452px;height:70px;background:var(--orange)}
.footer-band p{position:absolute;left:115px;font-size:5.6px;line-height:7px;color:var(--ink);width:318px}
.footer-strip{position:absolute;left:0;top:620px;width:452px;height:20px;background:linear-gradient(90deg,#1b1b1b,#444 45%,#1b1b1b)}

/* back */
.orange-rule{position:absolute;left:0;width:438px;height:3px;background:var(--orange)}
.back-intro{position:absolute;left:0;top:312px;width:196px;height:258px;background:linear-gradient(180deg,#fff,#dedede)}
.back-intro h3{position:absolute;left:13px;top:10px;font-family:"Oswald",sans-serif;font-weight:500;font-size:8.2px;line-height:9.5px;color:var(--ink)}
.back-intro h3 span{display:block;font-family:"PT Sans Narrow",sans-serif;font-weight:400;color:var(--orange);font-size:8px}
.back-intro p{position:absolute;left:13px;width:178px;font-size:5.9px;line-height:8px;color:#333}
.back-intro .phone{color:var(--orange);font-weight:700;font-size:8px}
.footnote{position:absolute;left:202px;top:536px;width:224px;font-size:4.6px;line-height:6px;color:#333}
.back-footer-dark{position:absolute;left:0;top:570px;width:220px;height:62px;background:linear-gradient(90deg,#111,#2b2b2b);clip-path:polygon(0 0,100% 0,94% 100%,0 100%)}
.back-footer-dark p{position:absolute;left:23px;font-family:"Oswald",sans-serif;color:var(--white);line-height:1}
.back-footer-dark em{font-style:normal;color:var(--orange)}
.back-footer-orange{position:absolute;left:206px;top:560px;width:232px;height:72px;background:var(--orange);clip-path:polygon(5% 0,100% 0,100% 100%,0 100%)}
.back-footer-orange h2{position:absolute;left:16px;top:11px;font-family:"Oswald",sans-serif;font-weight:500;font-size:19px;line-height:25px;white-space:nowrap}
.back-footer-orange .line1{color:var(--white)}
.back-footer-orange .line2{color:var(--ink);font-weight:400}
</style>
</head>
<body>

<section class="sheet sheet--front" aria-label="Flyer front">
  <div class="photo" role="img" aria-label="Three students lying on grass laughing while looking at a pink tablet"
       style="left:0;top:0;width:452px;height:220px;background:linear-gradient(160deg,#b9cf7a 0%,#d8c4a4 35%,#c98f7a 55%,#6e8f3a 80%,#4c7a2a 100%)"></div>
  <div class="brand" style="left:18px;top:30px"><span class="brand__dot"></span>KLT</div>

  <div class="headline">
    <div class="headline__orange"></div>
    <div class="headline__black"></div>
    <div class="headline__year">2017 FREE</div>
    <div class="headline__title">HSC PREPARATION WORKSHOP<br>AND SCHOLARSHIP OFFER</div>
    <div class="headline__tag tag--orange" style="top:22px">Limited spots available at both</div>
    <div class="headline__tag tag--white" style="top:36px">venues! Don't miss out!</div>
    <div class="headline__tag tag--orange" style="top:62px">This event could make all the Difference</div>
    <div class="headline__tag tag--white" style="top:76px">To your HSC Experience!</div>
  </div>

  <div class="info-panel">
    <h3>What will the day involve?</h3>
    <ul class="bullets" style="left:10px;top:24px;width:102px">
      <li>Establishing individual goals for the year ahead</li>
      <li>Developing the right mindset for the HSC</li>
      <li>Participating in case studies that simulate the Year 12 experience</li>
    </ul>
    <ul class="bullets" style="left:124px;top:24px;width:108px">
      <li>Understanding the importance of starting early and keeping up to date</li>
      <li>Strategies to increase the EFFICIENCY AND EFFECTIVENESS of your studies while decreasing levels of PROCRASTINATION</li>
    </ul>
    <p class="strong" style="left:10px;top:76px">Planning a BALANCED approach to studies and AVOIDING BURNOUT with:</p>
    <ul class="bullets" style="left:10px;top:86px;width:110px">
      <li>The 4 stages of examination preparation</li>
      <li>The 7 habits of highly effective students</li>
    </ul>
    <ul class="bullets" style="left:132px;top:86px;width:100px">
      <li>The 8 steps to Academic Success</li>
    </ul>
    <div class="reg-title" style="position:absolute;left:18px;top:110px">How to register:</div>
    <p style="left:18px;top:124px;width:212px;line-height:11px">Text 0400 123 456 with your name, email address and the session date and time you wish to attend.</p>
    <p class="strong" style="left:18px;top:150px">An email will then be sent confirming further details.</p>
  </div>

  <div class="sessions" style="left:244px;top:328px;width:200px">
    <h4>Presentation 1</h4>
    <div class="row row--orange"><span class="row__label" style="width:83px">Date</span><span class="row__value">Monday 3rd October, 2016</span></div>
    <div class="row row--orange"><span class="row__label" style="width:83px">Location</span><span class="row__value">Penrith</span></div>
    <div class="row row--orange"><span class="row__label" style="width:83px">time</span><span class="row__value">Session 1 – 10:00 – 1:00 (20 seats available)<br>Session 2 – 2:00 – 5:00 (20 seats available)</span></div>
    <div class="row row--orange"><span class="row__label" style="width:83px">Cost</span><span class="row__value">FREE*<br>Secure your spot with a $20 deposit that is<br>returned at the end of the presentation</span></div>
  </div>
  <div class="sessions" style="left:268px;top:426px;width:152px">
    <h4>Presentation 2</h4>
    <div class="row row--grey"><span class="row__label" style="width:64px">Date</span><span class="row__value">Monday 3rd October, 2016</span></div>
    <div class="row row--grey"><span class="row__label" style="width:64px">Location</span><span class="row__value">Penrith</span></div>
    <div class="row row--grey"><span class="row__label" style="width:64px">time</span><span class="row__value" style="font-size:4.4px;line-height:5.6px">Session 1 – 10:00 – 1:00 (20 seats available)<br>Session 2 – 2:00 – 5:00 (20 seats available)</span></div>
    <div class="row row--grey"><span class="row__label" style="width:64px;padding-top:8px;height:26px">Cost</span><span class="row__value" style="font-size:4.4px;line-height:5.6px">FREE*<br>Secure your spot with a $20 deposit that is<br>returned at the end of the presentation</span></div>
  </div>

  <div class="footer-band">
    <p style="top:11px">Turn over to read about the inaugural<br>Key Learning Track Scholarship Program</p>
    <p style="top:38px">"I have worked as both a teacher and tutor in Sydney and other parts of New South Wales for the last 7 years. I've helped many students achieve better marks than they thought possible. My aim has always been the same: I want students to have a life while completing their HSC and achieving their academic goals"</p>
  </div>
  <div class="footer-strip"></div>
  <div class="owner-photo" role="img" aria-label="Portrait of the business owner in a blue shirt, arms crossed"></div>
  <div class="owner-name">Daniel Marsh<br>Key Learning Track owner</div>
</section>

<section class="sheet sheet--back" aria-label="Flyer back">
  <div class="photo" role="img" aria-label="Group of cheerful teenagers jumping together under a blue sky"
       style="left:0;top:0;width:438px;height:196px;background:linear-gradient(180deg,#5f8fcf 0%,#a9c6e8 45%,#d7b26a 70%,#c9a052 100%)"></div>
  <div class="brand" style="left:18px;top:30px"><span class="brand__dot"></span>KLT</div>
  <div class="orange-rule" style="top:196px"></div>
  <svg class="photo" style="left:0;top:199px" width="438" height="110" viewBox="0 0 438 110" role="img" aria-label="Strip of four photos: a stressed student sitting, two students shaking hands, a student greeting a mentor, a student resting his head on a pile of books">
    <polygon points="0,0 118,0 98,110 0,110" fill="#7f8e9c"/>
    <polygon points="122,0 230,0 210,110 102,110" fill="#d98aa6"/>
    <polygon points="234,0 342,0 322,110 214,110" fill="#c9c6bd"/>
    <polygon points="346,0 438,0 438,110 326,110" fill="#8a7a66"/>
  </svg>
  <div class="orange-rule" style="top:309px"></div>

  <div class="back-intro">
    <h3>ATTEND THE FREE 2017 HSC PREPARATION<span>WORKSHOP TO FIND OUT MORE<br>INFORMATION ABOUT THE APPLICATION PROCESS</span></h3>
    <p style="top:70px">Key Learning Track is a venture with one objective: to change the world. We're going to do this one person at a time, helping individuals to achieve their goals in a number of ways.</p>
    <p style="top:118px">Throughout your HSC year, KLT will track your journey through a collection of surveys and small reflection activities and use the information to determine the scholarship recipients. Each scholarship can be awarded for a variety of reasons and the highest ATARs will not be the only determining factor.*</p>
    <p style="top:186px"><strong style="font-size:7.5px;color:var(--ink)">How to register:</strong><br>Text <span class="phone">0400 123 456</span> with your name, email address and the session date and time you wish to attend. An email will then be sent confirming further details.</p>
  </div>

  <div class="sessions" style="left:240px;top:316px;width:152px">
    <h4>Presentation 1</h4>
    <div class="row row--grey"><span class="row__label" style="background:var(--orange);color:var(--white);width:62px">Date</span><span class="row__value">Monday</span></div>
    <div class="row row--grey"><span class="row__label" style="background:var(--orange);color:var(--white);width:62px">Location</span><span class="row__value">Penrith</span></div>
    <div class="row row--grey"><span class="row__label" style="background:var(--orange);color:var(--white);width:62px;height:18px;padding-top:6px">Time</span><span class="row__value" style="font-size:4.6px;line-height:5.8px">Session 1 – 10:00 – 1:00<br>Session 2 – 2:00 – 5:00</span></div>
    <div class="row row--grey"><span class="row__label" style="background:var(--orange);color:var(--white);width:62px;height:24px;padding-top:8px">Cost</span><span class="row__value" style="font-size:4.4px;line-height:5.6px">FREE*<br>Secure your spot with a $20 deposit that<br>is returned at the end of the presentation</span></div>
  </div>
  <div class="sessions" style="left:240px;top:422px;width:152px">
    <h4>Presentation 2</h4>
    <div class="row row--grey"><span class="row__label" style="width:62px">Date</span><span class="row__value">Tuesday</span></div>
    <div class="row row--grey"><span class="row__label" style="width:62px">Location</span><span class="row__value">Burwood</span></div>
    <div class="row row--grey"><span class="row__label" style="width:62px">Time</span><span class="row__value" style="font-size:4.6px;line-height:5.8px">Session 1 – 10:00 – 1:00<br>Session 2 – 2:00 – 5:00</span></div>
    <div class="row row--grey"><span class="row__label" style="width:62px;height:24px;padding-top:8px">Cost</span><span class="row__value" style="font-size:4.4px;line-height:5.6px">FREE*<br>Secure your spot with a $20 deposit that is<br>returned at the end of the presentation</span></div>
  </div>

  <p class="footnote">*Many things can happen during the HSC year. Decisions can be made that affect your future. University is not the only pathway and scholarships can be awarded to students who choose alternative pathways including entering the workforce and studying at TAFE.</p>

  <div class="back-footer-dark">
    <p style="top:7px;font-size:13px">IN <em>2017</em>, THE PROGRAM'S</p>
    <p style="top:24px;font-size:15px;font-weight:600;color:var(--orange)">FIRST YEAR, 4 X $500</p>
    <p style="top:44px;font-size:11.5px">SCHOLARSHIPS ARE ON <em>OFFER</em></p>
  </div>
  <div class="back-footer-orange">
    <h2><span class="line1">KEY LEARNING TRACK</span><br><span class="line2">SCHOLARSHIP PROGRAM</span></h2>
  </div>
</section>

<div class="side-label side-label--front">FRONT</div>
<div class="side-label side-label--back">BACK</div>
</body>
</html>
```